FREE BBQ for life if you win our business with your creative menu design

Looking for a 11x17 size menu. we are a full service BBQ restaurant. We have an upscale environment as well as up scale service. We offer 5 star dinning at a casual price. we are on route 66 and are proud of that. we offer the finest smoked meats. Specializing in smoked pork beef and bison. we have an old barn wood decor. we only use oak to smoke our meats. use a lot of tarnished metal as well as some string nail art. Looking for a menu that goes along our style. i have attached as many pictures as i could to give you a fill of how we do it out here.
PLEASE USE THE 11"X17" MENU TEMPLATE ATTACHED IN THE PROJECT BRIEF.
Target Market(s)
Cool people and there families.
Industry/Entity Type
Business
Requirements
Must have
- I have attached the Current menu we use. File pollards menu pub. Those are all the Items. There will be some changes as we but together the new menu. The prices are changing. but that should be an easy change as we go.
Nice to have
- We are getting away from the lunch dinner menu and going to an all day menu. so rather than coming with toast or bun we will now be asking as an option. I have attached a menu i tried to make as a sample of how we will be doing it. new menu single page and new menu single page flame. These are ideas i had but could not really make it work. so use them as an idea of what we are looking for but be creative.

```html
<!DOCTYPE html>
<html lang="en">
<head>
<meta charset="utf-8">
<title>Pollards Barbeque Menu</title>
<link href="https://fonts.googleapis.com/css2?family=Rye&family=Open+Sans:wght@300;400;700&display=swap" rel="stylesheet">
<style>
:root{
  --frame:#3a281b;
  --frame-dark:#24180f;
  --parchment:#b98a53;
  --ink:#3b2614;
  --heading-fill:#d6ad74;
  --brand:#2f2a6e;
  --tack:#6b6b6b;
}
*{margin:0;padding:0;box-sizing:border-box}
html,body{width:782px;height:1200px;overflow:hidden;background:var(--frame-dark)}
.menu{position:relative;width:782px;height:1200px;font-family:"Open Sans",sans-serif;color:var(--ink)}
.menu-backdrop{position:absolute;inset:0}
.brand{position:absolute;left:72px;top:56px;width:290px;font-family:"Open Sans",sans-serif;font-weight:700;color:var(--brand);line-height:1}
.brand span{display:block}
.brand .brand-top{font-size:24px;letter-spacing:1px}
.brand .brand-main{font-size:46px;margin-top:4px;letter-spacing:1px}
.tack{position:absolute;left:728px;top:42px;width:30px;height:30px;border-radius:50%;background:var(--tack);border:3px solid #444}
.section{position:absolute;width:334px}
.col-left{left:53px}
.col-right{left:397px}
.section-title{position:absolute;width:334px;display:flex;align-items:center;justify-content:center;gap:12px}
.section-title h2{font-family:"Rye",serif;font-weight:400;font-size:24px;color:var(--heading-fill);-webkit-text-stroke:1px var(--ink);letter-spacing:1px;line-height:1}
.ornament{display:block;width:36px;height:12px;border-radius:50%;background:#8c6438}
.intro{font-size:10.6px;line-height:12.8px;font-weight:300;margin-bottom:7px}
.intro strong{display:block;font-size:10.6px;font-weight:700}
.item{margin-bottom:7px;font-size:9.6px;line-height:11.6px}
.item-row{display:flex;align-items:baseline;font-weight:700;font-size:9.8px}
.item-row .leader{flex:1;border-bottom:1.5px dotted var(--ink);margin:0 6px;transform:translateY(-2px)}
.item-note{font-weight:700;font-size:9.6px;padding-left:28px;margin-top:2px}
.wrap-builder{font-size:9.4px;line-height:11.6px}
.wrap-builder h3{font-size:9.8px;font-weight:700}
.wrap-builder b{font-weight:700}
</style>
</head>
<body>
<main class="menu">
  <svg class="menu-backdrop" width="782" height="1200" viewBox="0 0 782 1200" aria-hidden="true">
    <rect width="782" height="1200" fill="#24180f"/>
    <polygon fill="#3a281b" points="10,20 60,12 120,24 200,10 300,22 400,8 500,20 600,10 700,22 772,12 776,1190 8,1192"/>
    <polygon fill="#b98a53" points="30,40 90,44 160,36 260,46 360,36 460,44 560,34 660,46 740,36 756,44 756,1160 30,1160"/>
  </svg>

  <div class="brand"><span class="brand-top">POLLARDS</span><span class="brand-main">BARBEQUE</span></div>
  <span class="tack" role="img" aria-label="Metal tack"></span>

  <!-- Bison -->
  <div class="section-title col-left" style="top:204px;left:53px"><span class="ornament"></span><h2>BISON</h2><span class="ornament"></span></div>
  <section class="section col-left" style="top:236px">
    <p class="intro"><strong>Heart healthy</strong>Comes with 1 sides and your choice of Texas toast, Kaiser bun, Whole wheat bread or Glutton Free bread</p>
    <div class="item"><div class="item-row">BISON BRISTEK<span class="leader"></span>18.65</div>The belly of beast, smoked then sliced thin and grilled . Juicy and tender</div>
    <div class="item"><div class="item-row">BISON BURGUER<span class="leader"></span>18.65</div>Smoked then grilled served with pepper jack cheese lettuce tomato pickle toped with spicy ranch</div>
    <div class="item"><div class="item-row">BISON STEAK<span class="leader"></span>18.65</div>The belly of beast, smoked then sliced thin and grilled . Juicy and tender</div>
  </section>

  <!-- Smoked -->
  <div class="section-title col-left" style="top:404px;left:53px"><span class="ornament"></span><h2>SMOKED</h2><span class="ornament"></span></div>
  <section class="section col-left" style="top:436px">
    <p class="intro">Comes with 1 sides and your choice of Texas toast, Kaiser bun, Whole wheat bread or Glutton Free bread</p>
    <div class="item"><div class="item-row">BABY RACK RIBS . . . . . . . .&nbsp; FULL RACK&nbsp; 19.96 . . . HALF RACK&nbsp; 18.65</div>Tender to the bone, finger licking good, never need a knife, best ribs you'll ever have.</div>
    <div class="item"><div class="item-row">ST. LOUIS RIBS<span class="leader"></span>16.45</div>A nice big tender spare rib , slow smoked to tender that you can sink your teeth into.</div>
    <div class="item"><div class="item-row">BEEF BRISKET<span class="leader"></span>10.95</div>The most insane mouth watering smoky, moist, succulent piece of meat your mouth will ever have</div>
    <div class="item"><div class="item-row">PULLED PORK<span class="leader"></span>9.59</div>Smoked for 18-20 hrs. then pulled and mixed with our signature base barbeque sauce</div>
    <div class="item"><div class="item-row">SLICED PORK<span class="leader"></span>9.54</div>Smoked juicy tenderloin sliced thin then grilled per order</div>
    <div class="item"><div class="item-row">SMOKED TURKEY<span class="leader"></span>9.49</div>Breast meat smoked and sliced. Juicy and tender</div>
    <div class="item"><div class="item-row">SMOKED CHICKEN HALF<span class="leader"></span>13.59</div>Moist and juicy smoked Breast and thigh on the bone basted with our signature sauce on the grill</div>
    <div class="item"><div class="item-row">RIB EYE<span class="leader"></span>21.95</div>12oz juicy steak grilled to your desired temp</div>
  </section>

  <!-- Wraps -->
  <div class="section-title col-left" style="top:786px;left:53px"><span class="ornament"></span><h2>WRAPS</h2><span class="ornament"></span></div>
  <section class="section col-left wrap-builder" style="top:823px">
    <h3>DESIGN YOUR OWN CUSTOM WRAP</h3>
    <p><b>Pick your favorite meat:</b> Pork, beef, chicken, turkey.</p>
    <p><b>Pick your cheese:</b> Pepper Jack, cheddar, cottage cheese.</p>
    <p><b>Pick what's inside your wrap:</b> Lettuce, tomato, pickle, onion, banana peppers, cucumber, grilled veggies and green Chile.</p>
    <p><b>Pick your sauce:</b> Spicy Ranch, Reg. Ranch, Blue Cheese, Italian, Sour Cream, Thousand Island,<br>Hot BBQ sauce, Sweet BBQ sauce.</p>
  </section>

  <!-- PB Customs -->
  <div class="section-title col-left" style="top:948px;left:53px"><span class="ornament"></span><h2>PB CUSTOMS</h2><span class="ornament"></span></div>
  <section class="section col-left" style="top:990px">
    <div class="item"><div class="item-row">BBQ TACOS<span class="leader"></span>9.85</div>Three Tacos in blue and red shells with your choice of meat topped with-shredded lettuce and Pico-D –BBQ and Spicy ranch. (Excludes ribs and bison)<div class="item-note">TACO TUESDAY IS A MUST!&nbsp; 5.00 TACOS ALL DAY</div></div>
    <div class="item" style="margin-top:12px"><div class="item-row">ROWDY CHICKEN SANDWICH</div>Skinless boneless chicken breasts breaded fried, topped with pepper jack cheese, lettuce, tomato onion and pickles. On a buttery grilled Texas toast.</div>
  </section>

  <!-- Appetizers -->
  <div class="section-title col-right" style="top:102px;left:397px"><span class="ornament"></span><h2>APPETIZERS</h2><span class="ornament"></span></div>
  <section class="section col-right" style="top:135px">
    <p class="intro">Comes with 1 sides and your choice of Texas toast, Kaiser bun, Whole wheat bread or Glutton Free bread</p>
    <div class="item"><div class="item-row">BABY RACK RIBS . . . . . . . .&nbsp; FULL RACK&nbsp; 19.96 . . . HALF RACK&nbsp; 18.65</div>Tender to the bone, finger licking good, never need a knife, best ribs you'll ever have.</div>
    <div class="item"><div class="item-row">ST. LOUIS RIBS<span class="leader"></span>16.45</div>A nice big tender spare rib , slow smoked to tender that you can sink your teeth into.</div>
    <div class="item"><div class="item-row">BEEF BRISKET<span class="leader"></span>10.95</div>The most insane mouth watering smoky, moist, succulent piece of meat your mouth will ever have</div>
    <div class="item"><div class="item-row">PULLED PORK<span class="leader"></span>9.59</div></div>
  </section>

  <!-- Sides -->
  <div class="section-title col-right" style="top:328px;left:397px"><span class="ornament"></span><h2>SIDES</h2><span class="ornament"></span></div>
  <section class="section col-right wrap-builder" style="top:366px">
    <h3>DESIGN YOUR OWN CUSTOM WRAP</h3>
    <p><b>Pick your favorite meat:</b> Pork, beef, chicken, turkey.</p>
    <p><b>Pick your cheese:</b> Pepper Jack, cheddar, cottage cheese.</p>
    <p><b>Pick what's inside your wrap:</b> Lettuce, tomato, pickle, onion, banana peppers, cucumber, grilled veggies and green Chile.</p>
    <p><b>Pick your sauce:</b> Spicy Ranch, Reg. Ranch, Blue Cheese, Italian, Sour Cream, Thousand Island,<br>Hot BBQ sauce, Sweet BBQ sauce.</p>
  </section>

  <!-- Desserts -->
  <div class="section-title col-right" style="top:490px;left:397px"><span class="ornament"></span><h2>DESSERTS</h2><span class="ornament"></span></div>
  <section class="section col-right" style="top:532px">
    <div class="item"><div class="item-row">BBQ TACOS<span class="leader"></span></div>Three Tacos in blue and red shells with your choice of meat topped with-shredded lettuce and Pico-D –BBQ and Spicy ranch. (Excludes ribs and bison)<div class="item-note">TACO TUESDAY IS A MUST!&nbsp; 5.00 TACOS ALL DAY</div></div>
    <div class="item" style="margin-top:12px"><div class="item-row">ROWDY CHICKEN SANDWICH</div>Skinless boneless chicken breasts breaded fried, topped with pepper jack cheese, lettuce, tomato onion and pickles. On a buttery grilled Texas toast.</div>
  </section>

  <!-- Drinks -->
  <div class="section-title col-right" style="top:682px;left:397px"><span class="ornament"></span><h2>DRINKS</h2><span class="ornament"></span></div>
  <section class="section col-right" style="top:726px">
    <div class="item"><div class="item-row">BBQ TACOS<span class="leader"></span></div>Three Tacos in blue and red shells with your choice of meat topped with-shredded lettuce and Pico-D –BBQ and Spicy ranch. (Excludes ribs and bison)<div class="item-note">TACO TUESDAY IS A MUST!&nbsp; 5.00 TACOS ALL DAY</div></div>
    <div class="item" style="margin-top:12px"><div class="item-row">ROWDY CHICKEN SANDWICH</div>Skinless boneless chicken breasts breaded fried, topped with pepper jack cheese, lettuce, tomato onion and pickles. On a buttery grilled Texas toast.</div>
  </section>

  <!-- Salads -->
  <div class="section-title col-right" style="top:874px;left:397px"><span class="ornament"></span><h2>SALADS</h2><span class="ornament"></span></div>
  <section class="section col-right" style="top:916px">
    <div class="item"><div class="item-row">BBQ TACOS<span class="leader"></span></div>Three Tacos in blue and red shells with your choice of meat topped with-shredded lettuce and Pico-D –BBQ and Spicy ranch. (Excludes ribs and bison)<div class="item-note">TACO TUESDAY IS A MUST!&nbsp; 5.00 TACOS ALL DAY</div></div>
    <div class="item" style="margin-top:12px"><div class="item-row">ROWDY CHICKEN SANDWICH</div>Skinless boneless chicken breasts breaded fried, topped with pepper jack cheese, lettuce, tomato onion and pickles. On a buttery grilled Texas toast.</div>
  </section>
</main>
</body>
</html>
```